Minesweeper App Redesign

This project involves redesigning the UI of an existing app. Participants are free to use their imagination and creativity in coming up with a new design.

Here is the Android app.
https://apps.qorvanet.com/store/item/details?id=brelteko.tilepuzzler

Components should include:
1) The minefield and screen where the game is played.
2) The selection of levels to play.
3) A screen showing that the player stepped on a mine and lost.
4) A screen showing that the player won.
5) Settings screen (or the settings could be integrated into the play screen if there is a way to do it).
6) Global top scores screen.
7) Top scores on device.
8) App icon (512px by 512px).
8) Help/How To screen.

```html
<!DOCTYPE html>
<html lang="en">
<head>
<meta charset="utf-8">
<title>Tilepuzzler — UI Sheet, Page 1</title>
<link rel="stylesheet" href="https://fonts.googleapis.com/css2?family=Quicksand:wght@300;400;500&display=swap">
<style>
  :root {
    --ink: #58595b;
    --ink-soft: #8a8b8d;
    --line: #d9d9db;
    --frame: #c9c9cb;
    --ad: #939598;
    --tile-top: #f1f1f2;
    --tile-right: #d4d4d6;
    --tile-bottom: #e9e9ea;
    --tile-left: #dcdcde;
    --open-flag: #e7e7e8;
    --red: #e2403a;
    --green: #5aae3c;
    --teal: #1fb3a6;
    --orange: #f08a24;
    --mine: #4a4a4c;
    --sun: #f7cf3a;
    --badge: #f8df6e;
  }
  * { box-sizing: border-box; margin: 0; padding: 0; }
  html, body { width: 1101px; height: 1200px; overflow: hidden; background: #fff; }
  body { font-family: "Quicksand", "Helvetica Neue", sans-serif; color: var(--ink); font-weight: 300; }

  .sheet {
    position: relative; width: 1200px; height: 1308px;
    transform: scale(0.9175); transform-origin: 0 0;
  }

  .section-label {
    position: absolute; font-size: 21px; letter-spacing: 1px; white-space: nowrap;
    color: var(--ink);
  }
  .section-label--left { transform: rotate(-90deg); transform-origin: left top; }
  .section-label--right { transform: rotate(90deg); transform-origin: left top; }

  /* Wordmark */
  .wordmark {
    position: absolute; left: 165px; top: 150px; width: 362px;
    text-align: center; font-size: 38px; line-height: 44px; letter-spacing: 2px;
    font-weight: 400; color: var(--ink);
  }

  .app-icon {
    position: absolute; left: 262px; top: 394px; width: 168px; height: 167px;
    background: conic-gradient(from -45deg, var(--tile-top) 0 90deg, var(--tile-right) 90deg 180deg, var(--tile-bottom) 180deg 270deg, var(--tile-left) 270deg 360deg);
    display: flex; align-items: center; justify-content: center;
  }
  .app-icon__name { font-size: 19px; font-weight: 400; letter-spacing: 1px; color: var(--ink); }

  /* Phone screens */
  .screen { position: absolute; width: 416px; border: 1px solid var(--frame); background: #fff; overflow: hidden; }
  .screen--play { left: 651px; top: 14px; height: 623px; }
  .screen--lost { left: 139px; top: 664px; height: 624px; }
  .screen--menu { left: 651px; top: 662px; height: 626px; }

  .status-bar { position: absolute; left: 0; top: 0; width: 100%; height: 60px; }
  .status-bar__menu { position: absolute; left: 20px; top: 20px; width: 35px; height: 18px; }
  .status-bar__menu i { display: block; height: 2px; background: var(--ink-soft); margin-bottom: 6px; }
  .status-bar__count, .status-bar__time { position: absolute; top: 10px; font-size: 30px; letter-spacing: 1px; color: var(--ink-soft); }
  .status-bar__count { left: 124px; }
  .status-bar__time { left: 252px; }
  .status-bar__state { position: absolute; left: 187px; top: 9px; width: 38px; height: 38px; border-radius: 50%; }
  .status-bar__state--happy { background: var(--sun); }
  .status-bar__state--lost { background: #8c8d8f; }

  .ad-bar {
    position: absolute; left: 0; bottom: 0; width: 100%; height: 76px; background: var(--ad);
    color: #fff; font-size: 15px; letter-spacing: 2px; font-weight: 400;
    display: flex; align-items: center; justify-content: center;
  }

  .board { position: absolute; display: grid; grid-template-columns: repeat(8, 49px); grid-auto-rows: 49px; gap: 2.5px; }
  .screen--play .board { left: 3px; top: 81px; }
  .screen--lost .board { left: 2px; top: 81px; }

  .tile { background: conic-gradient(from -45deg, var(--tile-top) 0 90deg, var(--tile-right) 90deg 180deg, var(--tile-bottom) 180deg 270deg, var(--tile-left) 270deg 360deg); }
  .cell {
    border: 1px solid var(--line); background: #fff;
    display: flex; align-items: center; justify-content: center; font-size: 29px; line-height: 1;
  }
  .cell--flag { background: var(--open-flag); border-color: var(--open-flag); }
  .cell--hit { background: var(--red); border-color: var(--red); }
  .n1 { color: var(--green); }
  .n2 { color: var(--teal); }
  .n3 { color: var(--orange); }
  .n4 { color: var(--red); }
  .mine { width: 24px; height: 24px; border-radius: 50%; background: var(--mine); }
  .cell--hit .mine { background: #fff; }
  .flag { width: 22px; height: 22px; }

  /* Menu overlay */
  .menu-backdrop {
    position: absolute; left: 0; top: 0; width: 100%; height: 548px;
    background: linear-gradient(180deg, #fdfdfd 0%, #f8f8f8 30%, #fafafa 60%, #fdfdfd 100%);
  }
  .menu-close { position: absolute; left: 24px; top: 15px; width: 26px; height: 26px; }
  .menu-list { position: absolute; left: 0; top: 128px; width: 100%; list-style: none; text-align: center; }
  .menu-list li { font-size: 42px; letter-spacing: 3px; line-height: 64.5px; color: #4a4a4c; }

  .page-badge {
    position: absolute; left: 1116px; top: 1234px; width: 84px; height: 74px; background: var(--badge);
    display: flex; flex-direction: column; align-items: center; justify-content: center;
    font-size: 22px; line-height: 25px; letter-spacing: 1px; color: var(--ink); font-weight: 400;
  }
</style>
</head>
<body>
<svg width="0" height="0" style="position:absolute" aria-hidden="true">
  <defs>
    <symbol id="flag" viewBox="0 0 22 22">
      <rect x="3" y="2" width="2.5" height="19" fill="#6d6e70"/>
      <polygon points="5.5,2 20,8 5.5,14" fill="#e2403a"/>
    </symbol>
  </defs>
</svg>

<main class="sheet">
  <span class="section-label section-label--left" style="left:63px; top:257px;">LOGO/BRANDING</span>
  <span class="section-label section-label--left" style="left:63px; top:577px;">ICON/BRANDING</span>
  <span class="section-label section-label--left" style="left:66px; top:1057px;">HIT A MINE SCREEN</span>
  <span class="section-label section-label--right" style="left:1138px; top:118px;">PLAY SCREEN (BEGINNGER)</span>
  <span class="section-label section-label--right" style="left:1138px; top:853px;">MENU SCREEN</span>

  <div class="wordmark">TILEPUZZLER</div>

  <div class="app-icon"><span class="app-icon__name">TILEPUZZLER</span></div>

  <!-- Play screen -->
  <section class="screen screen--play">
    <header class="status-bar">
      <span class="status-bar__menu"><i></i><i></i><i></i></span>
      <span class="status-bar__count">10</span>
      <span class="status-bar__state status-bar__state--happy"></span>
      <span class="status-bar__time">0:32</span>
    </header>
    <div class="board">
      <span class="tile"></span><span class="tile"></span><span class="tile"></span><span class="tile"></span><span class="tile"></span><span class="tile"></span><span class="tile"></span><span class="tile"></span>
      <span class="tile"></span><span class="tile"></span><span class="tile"></span><span class="tile"></span><span class="tile"></span><span class="tile"></span><span class="tile"></span><span class="tile"></span>
      <span class="tile"></span><span class="tile"></span><span class="tile"></span><span class="tile"></span><span class="tile"></span><span class="tile"></span><span class="tile"></span><span class="tile"></span>
      <span class="tile"></span><span class="tile"></span><span class="tile"></span><span class="tile"></span><span class="tile"></span><span class="tile"></span><span class="tile"></span><span class="tile"></span>
      <span class="tile"></span><span class="tile"></span><span class="tile"></span><span class="tile"></span><span class="tile"></span><span class="tile"></span><span class="tile"></span><span class="tile"></span>
      <span class="tile"></span><span class="tile"></span><span class="tile"></span><span class="tile"></span><span class="tile"></span><span class="tile"></span><span class="tile"></span><span class="tile"></span>
      <span class="tile"></span><span class="tile"></span><span class="tile"></span><span class="tile"></span><span class="tile"></span><span class="tile"></span><span class="tile"></span><span class="tile"></span>
      <span class="tile"></span><span class="tile"></span><span class="tile"></span><span class="tile"></span><span class="tile"></span><span class="tile"></span><span class="tile"></span><span class="tile"></span>
    </div>
    <footer class="ad-bar">ADVERTISMENT</footer>
  </section>

  <!-- Lost screen -->
  <section class="screen screen--lost">
    <header class="status-bar">
      <span class="status-bar__menu"><i></i><i></i><i></i></span>
      <span class="status-bar__count">03</span>
      <span class="status-bar__state status-bar__state--lost"></span>
      <span class="status-bar__time">0:32</span>
    </header>
    <div class="board">
      <span class="tile"></span><span class="tile"></span><span class="cell cell--hit"><span class="mine"></span></span><span class="tile"></span><span class="cell n1">1</span><span class="cell n1">1</span><span class="cell"></span><span class="cell"></span>
      <span class="tile"></span><span class="tile"></span><span class="cell"><span class="mine"></span></span><span class="cell n4">4</span><span class="cell cell--flag"><svg class="flag"><use href="#flag"/></svg></span><span class="cell n1">1</span><span class="cell"></span><span class="cell"></span>
      <span class="cell"><span class="mine"></span></span><span class="tile"></span><span class="tile"></span><span class="cell cell--flag"><svg class="flag"><use href="#flag"/></svg></span><span class="cell n2">2</span><span class="cell n1">1</span><span class="cell n2">2</span><span class="cell n2">2</span>
      <span class="cell n1">1</span><span class="cell n1">1</span><span class="cell n1">1</span><span class="cell n1">1</span><span class="cell n1">1</span><span class="cell n1">1</span><span class="cell cell--flag"><svg class="flag"><use href="#flag"/></svg></span><span class="cell cell--flag"><svg class="flag"><use href="#flag"/></svg></span>
      <span class="cell"></span><span class="cell n1">1</span><span class="cell n1">1</span><span class="cell n1">1</span><span class="cell"></span><span class="cell n1">1</span><span class="cell n2">2</span><span class="cell n2">2</span>
      <span class="cell"></span><span class="cell n2">2</span><span class="cell cell--flag"><svg class="flag"><use href="#flag"/></svg></span><span class="cell n2">2</span><span class="cell"></span><span class="cell"></span><span class="cell"></span><span class="cell"></span>
      <span class="cell"></span><span class="cell n3">3</span><span class="cell cell--flag"><svg class="flag"><use href="#flag"/></svg></span><span class="cell n3">3</span><span class="cell"></span><span class="cell"></span><span class="cell"></span><span class="cell"></span>
      <span class="cell"></span><span class="cell n2">2</span><span class="cell cell--flag"><svg class="flag"><use href="#flag"/></svg></span><span class="cell n2">2</span><span class="cell"></span><span class="cell"></span><span class="cell"></span><span class="cell"></span>
    </div>
    <footer class="ad-bar">ADVERTISMENT</footer>
  </section>

  <!-- Menu screen -->
  <section class="screen screen--menu">
    <div class="menu-backdrop" role="img" aria-label="Blurred game board behind the menu"></div>
    <svg class="menu-close" viewBox="0 0 26 26" aria-label="Close menu">
      <path d="M1 1 L25 25 M25 1 L1 25" stroke="#6d6e70" stroke-width="2" fill="none"/>
    </svg>
    <ul class="menu-list">
      <li>LEVEL</li>
      <li>SCORES</li>
      <li>SETTINGS</li>
      <li>HELP</li>
    </ul>
    <footer class="ad-bar">ADVERTISMENT</footer>
  </section>

  <div class="page-badge"><span>PAGE</span><span>1 of 3</span></div>
</main>
</body>
</html>
```